A4 Single Sided Brochure Folder Design Technical Company

We are a technical company based in the UK, working worldwide for Power Distribution companies.

We have technical literature and need a folder to present these in. The design should be very simple and clean using our logo and "Innovative Utility Solutions"

Our website brenvox.com gives and idea of the business but don't follow the look of the website as we will be redoing shortly.

Requirements
Must have
• Logo and Strap Line
Nice to have
• Clean, easy to print and timeless
Should not have
• Shouldn't be fashionable, we certainly aren't

```html
<!DOCTYPE html>
<html lang="en">
<head>
<meta charset="utf-8">
<title>Brenvox Presentation Folder</title>
<link href="https://fonts.googleapis.com/css2?family=Lato:wght@300;400;700&display=swap" rel="stylesheet">
<style>
  :root {
    --brand-magenta: #b92d8a;
    --paper: #ffffff;
    --backdrop: #e8e5e1;
    --reverse-text: #ffffff;
  }
  html, body {
    margin: 0;
    padding: 0;
    width: 1200px;
    height: 1200px;
    overflow: hidden;
    background: var(--backdrop);
  }
  .canvas {
    position: relative;
    width: 1200px;
    height: 1200px;
    font-family: "Lato", sans-serif;
  }
  .folder-cover {
    position: absolute;
    left: 118px;
    top: 202px;
    width: 982px;
    height: 684px;
    background: var(--paper);
    box-shadow: 0 2px 6px rgba(0,0,0,0.12);
  }
  .brand-name {
    position: absolute;
    left: 682px;
    top: 504px;
    margin: 0;
    font-weight: 400;
    font-size: 56px;
    line-height: 1;
    color: var(--brand-magenta);
    letter-spacing: 0.5px;
  }
  .footer-band {
    position: absolute;
    left: 0;
    top: 609px;
    width: 100%;
    height: 48px;
    background: var(--brand-magenta);
    color: var(--reverse-text);
  }
  .website {
    position: absolute;
    left: 39px;
    top: 17px;
    font-size: 10px;
    font-weight: 700;
    letter-spacing: -0.3px;
  }
  .strapline {
    position: absolute;
    right: 26px;
    top: 8px;
    font-size: 26px;
    font-weight: 300;
    letter-spacing: 0.3px;
  }
  .pocket {
    position: absolute;
    left: 0;
    top: 0;
  }
</style>
</head>
<body>
  <div class="canvas">
    <div class="folder-cover">
      <p class="brand-name">Brenvox</p>
      <div class="footer-band">
        <span class="website">www.brenvox.com</span>
        <span class="strapline">Innovative Utility Solutions</span>
      </div>
    </div>
    <svg class="pocket" width="1200" height="1200" viewBox="0 0 1200 1200" aria-hidden="true">
      <polygon class="pocket-glue-flap" points="83,898 118,887 118,1090 83,1084" fill="var(--brand-magenta)"/>
      <polygon class="pocket-panel" points="118,887 608,887 542,1090 118,1090" fill="var(--brand-magenta)"/>
      <line x1="118" y1="887" x2="118" y2="1090" stroke="rgba(0,0,0,0.12)" stroke-width="1"/>
    </svg>
  </div>
</body>
</html>
```